Candle Rental Business seeks new website design

We need a new website design for a Candle hire business. The business rents out pillar candles for events such as weddings and corporate events. Our main target market is weddings. The business name is Hire a Lantern. The business name does not have a logo design.

We would like a website that is light in colours and creates a warm atmosphere. The design needs to be elegant and upmarket. There are different size candles that we hire out, ranging from 10cm diameter to 20cm diameter, flat, tall etc. All our candles are white in colour. Its just the size that differs.

We would also like to include a section for hiring out decor such as glassvases, candlebras, overlays and chairs sachets, chair covers. However, this is not the businesses main focus but an additional offering to customers.

Target Market(s)

Wedding venues and brides. Corporate events. School dances.

Industry/Entity Type

Hospitality

Logo Text

Hire a Lantern

Number of Pages Required

1 page

Font styles to use
Sans Serif
Script

Requirements
Must have
• Pictures of pillar candles. Plain white candles. The website must centre around candles.
Nice to have
• Different examples of candle centrepieces
Should not have
• Pictures must not be of brides. Pictures of surrounding is perferable.

```html
<!DOCTYPE html>
<html lang="en">
<head>
<meta charset="utf-8">
<title>Hire a Lantern</title>
<link href="https://fonts.googleapis.com/css2?family=Roboto+Slab:wght@300;400&family=Kaushan+Script&display=swap" rel="stylesheet">
<style>
  :root {
    --gold: #e2a82c;
    --accent: #c4531d;
    --green: #95ad4f;
    --cream: #f5f1e8;
    --text: #6d6d6d;
    --dark: #3d3d3d;
    --white: #ffffff;
  }
  * { margin: 0; padding: 0; box-sizing: border-box; }
  html, body { width: 768px; height: 1200px; overflow: hidden; background: var(--white); }
  body { position: relative; font-family: "Roboto Slab", Georgia, serif; font-weight: 300; color: var(--text); }
  .abs { position: absolute; }

  /* Hero */
  .hero { left: 0; top: 0; width: 768px; height: 349px;
    background: radial-gradient(ellipse at 45% 35%, #f6e6b8 0%, #e6c46e 40%, #c9952f 75%, #a8771f 100%); }
  .nav { left: 84px; top: 0; width: 600px; height: 42px; background: var(--gold); }
  .nav a { position: absolute; top: 14px; font-size: 10.5px; font-weight: 400; color: var(--white); text-decoration: none; }
  .brand { left: 296px; top: 0; width: 160px; height: 70px; background: var(--white);
    border-radius: 0 0 80px 80px / 0 0 36px 36px; display: flex; align-items: flex-start; justify-content: center; padding-top: 17px; }
  .brand span { font-family: "Roboto Slab", Georgia, serif; font-weight: 400; font-size: 19px; color: var(--accent); }
  .hero-title { left: 0; width: 768px; top: 156px; text-align: center; font-family: "Kaushan Script", cursive;
    font-size: 31px; color: var(--white); text-shadow: 0 1px 4px rgba(120,70,0,.35); }
  .thumb { top: 286px; width: 85px; height: 44px; border: 2px solid var(--white); }
  .thumb-pointer { left: 279px; top: 280px; width: 0; height: 0; border-left: 6px solid transparent; border-right: 6px solid transparent; border-bottom: 6px solid var(--white); }

  /* About */
  .about-title { left: 0; width: 768px; top: 372px; text-align: center; font-size: 16px; color: var(--dark); }
  .about-title em, .gallery-title em { font-style: normal; color: var(--accent); }
  .about-copy { left: 84px; width: 600px; top: 407px; text-align: center; font-size: 8.6px; line-height: 15.6px; }

  /* Services */
  .services { left: 0; top: 484px; width: 768px; height: 338px; background: var(--cream); }
  .card { background: var(--white); }
  .card h3 { position: absolute; font-weight: 400; font-size: 16px; color: var(--accent); }
  .card p { position: absolute; font-size: 7.4px; line-height: 13.2px; }
  .btn { position: absolute; height: 17px; padding: 0 10px; background: var(--green); color: var(--white);
    font-size: 7.4px; line-height: 17px; font-weight: 300; }

  /* Gallery */
  .gallery-title { left: 84px; top: 845px; font-size: 16px; color: var(--dark); }
  .photo { width: 127px; height: 71px; }
  .testimonial { left: 524px; top: 857px; width: 160px; height: 176px; background: var(--green); }
  .avatar { left: 578px; top: 845px; width: 52px; height: 52px; border-radius: 50%; border: 2px solid var(--white);
    background: radial-gradient(circle at 50% 40%, #d9b494, #6a4a34); }
  .quote { left: 534px; width: 140px; top: 907px; text-align: center; font-size: 7.4px; line-height: 13.2px; color: var(--white); }
  .quote-name { left: 524px; width: 160px; top: 990px; text-align: center; font-size: 9px; font-weight: 400; color: var(--white); }
  .dot { top: 1017px; height: 2px; width: 18px; background: rgba(255,255,255,.45); }

  /* Footer */
  .footer { left: 0; top: 1058px; width: 768px; height: 142px; background: var(--gold); }
  .footer h4 { position: absolute; font-weight: 400; font-size: 11.5px; color: var(--accent); }
  .footer p { position: absolute; font-size: 8.6px; line-height: 13.5px; color: var(--white); font-weight: 400; }
  .contact { left: 0; width: 768px; text-align: center; color: var(--white); font-weight: 400; }
  .social { top: 1104px; width: 18px; height: 18px; background: rgba(255,255,255,.85); }
  .rule { left: 84px; top: 1142px; width: 600px; height: 1px; background: rgba(255,255,255,.35); }
  .footer-nav { left: 0; width: 768px; top: 1156px; text-align: center; font-size: 8.6px; color: var(--white); font-weight: 400; }
  .footer-nav span { margin: 0 5px; }
  .copyright { left: 0; width: 768px; top: 1173px; text-align: center; font-size: 8.6px; color: var(--white); font-weight: 400; }
</style>
</head>
<body>

<div class="abs hero" role="img" aria-label="White pillar candles glowing among gold ribbons, beads and small gift boxes"></div>
<nav class="abs nav">
  <a style="left:23px">Home</a>
  <a style="left:81px">About Us</a>
  <a style="left:154px">Services</a>
  <a style="left:394px">Products</a>
  <a style="left:465px">Gallery</a>
  <a style="left:528px">Contact Us</a>
</nav>
<div class="abs brand"><span>Hire a Lantern</span></div>
<h1 class="abs hero-title" style="font-weight:400">Meaningful gift at a friendly price point</h1>
<div class="abs thumb-pointer"></div>
<div class="abs thumb" style="left:242px;background:linear-gradient(135deg,#f4d46a,#e8b23a 60%,#fff3d0)" role="img" aria-label="Slide preview: candles with gold ribbons"></div>
<div class="abs thumb" style="left:342px;background:linear-gradient(135deg,#3b2a22,#8a6a52 50%,#c9c4be)" role="img" aria-label="Slide preview: dark pillar candle"></div>
<div class="abs thumb" style="left:442px;background:linear-gradient(135deg,#c9d6ee,#e8d6e6 60%,#f3c7d3)" role="img" aria-label="Slide preview: pastel candles"></div>

<h2 class="abs about-title" style="font-weight:300">About <em>Hire a Lantern</em></h2>
<p class="abs about-copy">We are a family owned and operated company and began making decorative candles for all occasions. All of our candles are individually hand made in our candle studio, situated in Elmsby, outside Northgate. Our wax is local and of a very high quality, and dripless! Our wax is also made with a high melting point, which means it will not melt or bend in hot temperatures.</p>

<section class="abs services"></section>
<div class="abs card" style="left:84px;top:509px;width:225px;height:295px">
  <div class="abs" style="left:12px;top:11px;width:201px;height:120px;background:linear-gradient(135deg,#9c8a6a,#e9e6e0 45%,#cfd6d8 70%,#5fa0b8)" role="img" aria-label="Tall white pillar candles with wine glasses on a table"></div>
  <h3 style="left:12px;top:143px">Hire Candles</h3>
  <p style="left:12px;top:168px;width:202px">Do you love using candles for your events but tired of sorting old used candles or buying expensive candles. Believe it or not you can now rent candles.All our candles come in different sizes and heights.You can add the ambience of candlelight to your event of wedding ceremony without the worry over dripping wax or open candle flames.</p>
  <span class="btn" style="left:12px;top:266px">Read More</span>
</div>
<div class="abs card" style="left:321px;top:509px;width:363px;height:141px">
  <h3 style="left:12px;top:7px">Personalised Candles</h3>
  <p style="left:12px;top:35px;width:210px">Hire a Lantern provides the opportunity to give a thoughtful, meaningful gift at a friendly price point. This unique gift conveys the time and care you put into creating it. The recipient will enjoy the beautiful presentation and be reminded of the sentiment...</p>
  <span class="btn" style="left:12px;top:112px">Read More</span>
  <div class="abs" style="left:229px;top:10px;width:124px;height:123px;background:linear-gradient(135deg,#ececec,#f3e9d8 50%,#d8d8d8)" role="img" aria-label="Two candles in glass jars with printed labels"></div>
</div>
<div class="abs card" style="left:321px;top:663px;width:363px;height:141px">
  <h3 style="left:12px;top:7px">Décor Hire</h3>
  <p style="left:12px;top:35px;width:210px">We hire a selection of overlays, chair sachets and chair covers as well as glassware and candelabras to compliment your décor.</p>
  <span class="btn" style="left:12px;top:85px">Read More</span>
  <div class="abs" style="left:232px;top:11px;width:120px;height:119px;background:radial-gradient(circle at 50% 55%,#d9d48a,#5d7a3a 45%,#5a2a22 80%)" role="img" aria-label="Table centrepiece with candle, glassware and white flowers"></div>
</div>

<h2 class="abs gallery-title" style="font-weight:300">Our <em>Photo Gallery</em></h2>
<div class="abs photo" style="left:84px;top:878px;background:linear-gradient(135deg,#5a3a2a,#e8dccb 50%,#b89a6a)" role="img" aria-label="Candlesticks and flowers on a dining table"></div>
<div class="abs photo" style="left:223px;top:878px;background:linear-gradient(135deg,#0d3a6a,#3aa6d8 50%,#0a2a4a)" role="img" aria-label="Reception hall with blue lighting and candles"></div>
<div class="abs photo" style="left:362px;top:878px;background:radial-gradient(circle at 40% 50%,#f2d9a0,#8a6a3a 40%,#2a1e12)" role="img" aria-label="Single candle glowing in a dim room"></div>
<div class="abs photo" style="left:84px;top:962px;background:radial-gradient(circle at 50% 55%,#e6c27a,#6a4a24 45%,#1e140c)" role="img" aria-label="Candelabra with tall white candles"></div>
<div class="abs photo" style="left:223px;top:962px;background:radial-gradient(circle at 50% 65%,#f0dcc0,#8a5a34 45%,#241812)" role="img" aria-label="Candlelit table with white flower arrangements"></div>
<div class="abs photo" style="left:362px;top:962px;background:linear-gradient(135deg,#4a3a30,#e8e2d8 55%,#c0a890)" role="img" aria-label="Candle ceremony table setting"></div>

<div class="abs testimonial"></div>
<div class="abs avatar" role="img" aria-label="Customer portrait"></div>
<p class="abs quote">"There are many variations of passages of Lorem Ipsum available, but the majority have suffered alteration in some form, by injected humour, or randomised words which don't look even slightly believable."</p>
<p class="abs quote-name">Mara Lindell</p>
<div class="abs dot" style="left:574px;background:var(--white)"></div>
<div class="abs dot" style="left:595px"></div>
<div class="abs dot" style="left:615px"></div>

<footer class="abs footer">
  <h4 style="left:85px;top:20px">Location</h4>
  <p style="left:85px;top:38px;width:160px">Simply dummy text printing typesetting AT 12356</p>
  <h4 style="right:84px;top:20px">Follow us</h4>
</footer>
<div class="abs contact" style="top:1085px;font-size:11.5px">+123 555 0148</div>
<div class="abs contact" style="top:1101px;font-size:12px">hello@lanternhire.example</div>
<div class="abs social" style="left:586px" role="img" aria-label="Social link"></div>
<div class="abs social" style="left:612px" role="img" aria-label="Social link"></div>
<div class="abs social" style="left:638px" role="img" aria-label="Social link"></div>
<div class="abs social" style="left:665px" role="img" aria-label="Social link"></div>
<div class="abs rule"></div>
<div class="abs footer-nav">Home<span>I</span>About Us<span>I</span>Services<span>I</span>Products<span>I</span>Gallery<span>I</span>Contact Us</div>
<div class="abs copyright">© 2016 Hire a Lantern, All Rights Reserved</div>

</body>
</html>
```